Website Design for two swimming school brands

Looking for a modern, engaging website design for my new business Every Stroke Water Learning. Within that business I have two current brands:
Every Stroke Swim and Yard Paddle
My current website (www.yardpaddle.net) has most of the info you'll need. Feel free to also use my socials for content.
Looking for someone to do the initial design/setup and then hand over full control to me with no ongoing fees or charges (except for hosting), and I'm responsible for all future changes. Ideally made and then can be edited in google sites but open to other options.

Website requirements are quite simple for both pages.
For the Yard Paddle page, I'd like the same info and features that are on my current website presented in a fresh way.
For the Every Stroke page, I'd like to see your concepts for design and possible sections, but it'll be roughly the same as the yard paddle one. I will upload a document soon for text and sections and other information to go on the Every stroke swim page.

For clarity the difference between the business' is one goes out to people's home pools and the other hires out lane space in public pool to conduct lessons.
I'd like a lighter theme for the Yard Paddle Website and a Darker one for the Every Stroke.
Both pages needs to be accessible with picture descriptions for screen reader and other similar features.

I currently use Bookora for all my inquiry, booking and payment functions so the website would need to be compatible with their widgets.

Have a look at the MockUp v2 or the business card design to get the concept of two different brandings working together.

Some text from the Every Stroke Swim Page can be found in this document:
https://docs.example-files.net/document/d/7QpaLmRvXc2TnWb8KdYs4FgHe9JuZoNi3VcXaBt/edit?usp=sharing
-
Feel free to ask any further questions.
Updates

Target Market(s)

Families and disability service providers

Industry/Entity Type

Sports and Recreation

Coding

Coded - Design and coding required

Number of Pages Required

4 page

Requirements
Must have
• Engaging design, ability to put in widgets into website, cross links between two business
Nice to have
• Common elements across the two pages but also points of difference

```html
<!DOCTYPE html>
<html lang="en">
<head>
<meta charset="utf-8">
<title>Yard Paddle - Every Stroke Water Learning</title>
<link href="https://fonts.googleapis.com/css2?family=Roboto:wght@400;500;700&display=swap" rel="stylesheet">
<style>
  :root {
    --bg: #dff2f1;
    --white: #ffffff;
    --teal: #17a88f;
    --teal-dark: #0b8a6c;
    --teal-light: #a8dcc0;
    --blue: #0a73c7;
    --blue-nav: #0a8ed6;
    --blue-deep: #3757a8;
    --purple: #4a3590;
    --purple-light: #5c4ea5;
    --sidebar: #f1f1f1;
    --ink: #222222;
    --ink-soft: #333333;
  }
  * { box-sizing: border-box; margin: 0; padding: 0; }
  html, body { width: 947px; height: 1200px; overflow: hidden; }
  body { background: var(--bg); font-family: "Roboto", Arial, sans-serif; color: var(--ink); }
  .page { position: absolute; left: 28px; top: 6px; width: 890px; background: var(--white); }

  .site-header { height: 200px; display: flex; flex-direction: column; align-items: center; justify-content: center; gap: 16px; }
  .brand { display: flex; align-items: center; gap: 10px; color: var(--teal); font-weight: 500; font-size: 30px; letter-spacing: 0.5px; }
  .brand-mark { width: 18px; height: 18px; background: var(--teal); }
  .tagline { color: var(--blue); font-weight: 700; font-size: 11px; letter-spacing: 0.3px; }

  .main-nav { height: 36px; background: var(--blue-nav); display: flex; font-size: 12.5px; }
  .main-nav a { color: var(--white); text-decoration: none; padding: 0 19px; display: flex; align-items: center; }
  .main-nav a.current { background: var(--blue); font-weight: 700; }

  .content { display: flex; height: 811px; }
  .primary { width: 622px; padding: 30px 17px 0; }
  .sidebar { flex: 1; background: var(--sidebar); padding: 30px 17px 0; }

  .bar-title { background: var(--blue); color: var(--white); font-weight: 700; font-size: 12px; height: 37px; display: flex; align-items: center; padding: 0 17px; }
  .features { list-style: disc; padding: 20px 0 0 34px; font-size: 15px; line-height: 22px; color: var(--ink-soft); }
  .features .free { color: var(--teal); }
  .features .free b { font-weight: 700; }

  .tiles { margin-top: 36px; display: grid; grid-template-columns: 294px 294px; grid-template-rows: 196px 206px; }
  .photo { width: 100%; height: 100%; }
  .photo-pool { background: linear-gradient(135deg, #1fa7c9, #38c4de 50%, #1b86b0); }
  .photo-family { background: linear-gradient(160deg, #7a8a7d, #c9d6d3 45%, #8fc7d3 70%, #e4e4e4); }
  .tile { color: var(--white); display: flex; flex-direction: column; align-items: center; text-align: center; padding: 30px 22px 0; }
  .tile-adults { background: linear-gradient(135deg, var(--blue-deep), #1f7ac7); }
  .tile-disability { background: linear-gradient(135deg, var(--purple-light), var(--purple)); }
  .tile h3 { font-size: 17px; font-weight: 700; margin: 28px 0 14px; }
  .tile p { font-size: 11.5px; line-height: 15px; }

  .crosslink { text-align: center; margin-top: 56px; font-weight: 700; font-size: 17px; color: var(--ink-soft); }
  .crosslink p + p { margin-top: 22px; }
  .crosslink a { color: var(--teal); text-decoration: none; }

  .card-children { height: 202px; background: linear-gradient(135deg, var(--teal-light), #3fa884 60%, var(--teal-dark)); color: var(--white); text-align: center; padding: 30px 26px 0; }
  .card-children h3 { font-size: 17px; font-weight: 700; margin: 24px 0 22px; }
  .card-children p { font-size: 11.5px; line-height: 15px; }
  .come-title { margin-top: 26px; background: linear-gradient(90deg, var(--purple), var(--purple-light)); color: var(--white); font-size: 11.5px; font-weight: 700; height: 37px; display: flex; align-items: center; padding: 0 17px; }
  .venues { list-style: disc; padding: 16px 0 0 34px; font-size: 12px; line-height: 18px; color: var(--ink); }
  .venues b { font-weight: 700; }

  .site-footer { height: 118px; background: linear-gradient(90deg, var(--purple), var(--purple-light)); color: var(--white); text-align: center; padding-top: 34px; font-size: 11.5px; }
  .site-footer a { color: var(--teal); text-decoration: none; }
  .social { display: flex; justify-content: center; gap: 14px; margin-top: 14px; }
  .social span { width: 20px; height: 20px; border-radius: 50%; background: var(--teal); }

  .copyright { position: absolute; top: 1170px; width: 947px; text-align: center; font-size: 12px; color: var(--ink-soft); }
</style>
</head>
<body>
<div class="page">
  <header class="site-header">
    <div class="brand"><span class="brand-mark"></span>YARDPADDLE</div>
    <div class="tagline">EVERY STROKE WATER LEARNING</div>
  </header>
  <nav class="main-nav">
    <a class="current" href="#">Yard Paddle</a>
    <a href="#">Every Stroke Swim</a>
  </nav>
  <div class="content">
    <main class="primary">
      <h2 class="bar-title">Mobile Swimming Lessons for all Ages and Abilities</h2>
      <ul class="features">
        <li>Professional Instructor with over 10 years experience</li>
        <li>At a time and place that works for you</li>
        <li>Individualised lesson structure based on the swimmers' needs</li>
        <li>Group and Individual Lessons available</li>
        <li>Lessons in your Own Pool</li>
        <li class="free"><b>FREE</b> in-home pool and swimmer assessment</li>
      </ul>
      <section class="tiles">
        <div class="photo photo-pool" role="img" aria-label="Older woman swimming with a kickboard in a blue pool"></div>
        <div class="tile tile-adults">
          <svg width="46" height="54" viewBox="0 0 46 54" aria-hidden="true"><circle cx="23" cy="13" r="12" fill="#fff"/><path d="M2 54v-8c0-11 8-17 21-17s21 6 21 17v8z" fill="#fff"/></svg>
          <h3>Adults</h3>
          <p>Helping adults learn, whether for the first time or now that they want to try it out again</p>
        </div>
        <div class="tile tile-disability">
          <svg width="46" height="54" viewBox="0 0 46 54" aria-hidden="true"><circle cx="23" cy="13" r="12" fill="#fff"/><path d="M2 54v-8c0-11 8-17 21-17s21 6 21 17v8z" fill="#fff"/></svg>
          <h3>People with a Disability</h3>
          <p>Enabling children and adults to overcome the challenges their disability presents, helping them achieve their goals</p>
        </div>
        <div class="photo photo-family" role="img" aria-label="Family of four standing beside their backyard pool"></div>
      </section>
      <div class="crosslink">
        <p>Looking for Lessons in a public or other private pool?</p>
        <p>Check out <a href="#">Every Stroke Swim</a></p>
      </div>
    </main>
    <aside class="sidebar">
      <div class="card-children">
        <svg width="38" height="52" viewBox="0 0 38 52" aria-hidden="true"><circle cx="19" cy="7" r="7" fill="#fff"/><path d="M2 14l5-2 9 8h6l9-8 5 2-10 12v26h-6V38h-2v14h-6V26z" fill="#fff"/></svg>
        <h3>Children &amp; Teenagers</h3>
        <p>Helping every child no matter their age** reach their full potential.</p>
      </div>
      <h2 class="come-title">We come to you:</h2>
      <ul class="venues">
        <li><b>Backyard Swimming Pools</b></li>
        <li><b>Apartment Centre Pools</b></li>
        <li><b>Hydrotherapy and Public Pools</b> (if lane hire is available)</li>
        <li><b>FREE</b> home pool and swimmer assessment</li>
      </ul>
    </aside>
  </div>
  <footer class="site-footer">
    <p>Meeting you where you are, helping you reach your goals: <a href="#">northside@yardpaddle.net</a></p>
    <div class="social"><span role="img" aria-label="Social profile one"></span><span role="img" aria-label="Social profile two"></span></div>
  </footer>
</div>
<p class="copyright">www.yardpaddle.net © 2022</p>
</body>
</html>
```